RTB CONTRACTING

I am looking for a logo/design for my business. Would like some unique symbol, would also like it to be double sided. On the back perhaps 3 pictures of some work we have done. I will attach some photos.

I would also like the colours to be orange and black or a dark grey and Orange.

Only writing I would like to see are:

(Contact number) 416-382-7164
(Name) Derek Holloway
(Email) dholloway@mailbox-example.ca

```html
<!DOCTYPE html>
<html lang="en">
<head>
<meta charset="utf-8">
<title>RTB Contracting — Business Card</title>
<link rel="stylesheet" href="https://fonts.googleapis.com/css2?family=Cinzel:wght@600&family=Exo+2:wght@400;500&display=swap">
<style>
  :root {
    --card-black: #050505;
    --brand-orange: #e85e21;
    --paper-white: #ffffff;
    --ghost-grey: #262626;
    --photo-tone: #3a3430;
    --stage: #e9e6e1;
  }
  html, body {
    margin: 0;
    width: 1200px;
    height: 870px;
    overflow: hidden;
    background: var(--stage);
  }
  .stage {
    position: relative;
    width: 1200px;
    height: 870px;
  }
  .card {
    position: absolute;
    top: 85px;
    width: 400px;
    height: 700px;
    background: var(--card-black);
    overflow: hidden;
    box-shadow: 0 6px 18px rgba(0,0,0,0.25);
  }
  .card--front { left: 150px; }
  .card--back { left: 650px; }
  .card__frame {
    position: absolute;
    inset: 0;
  }
  .brand {
    position: absolute;
    left: 0;
    right: 0;
    display: flex;
    flex-direction: column;
    align-items: center;
    font-family: "Cinzel", Georgia, serif;
    font-weight: 600;
    color: var(--paper-white);
    letter-spacing: 1px;
    white-space: nowrap;
  }
  .brand__square {
    background: var(--brand-orange);
    flex: none;
  }
  .card--front .brand { top: 100px; font-size: 26px; gap: 14px; }
  .card--front .brand__square { width: 50px; height: 50px; }
  .holder {
    position: absolute;
    top: 290px;
    left: 0;
    right: 0;
    text-align: center;
    font-family: "Exo 2", Arial, sans-serif;
    color: var(--paper-white);
  }
  .holder__name {
    font-size: 24px;
    font-weight: 500;
    letter-spacing: 1px;
    margin: 0;
  }
  .holder__role {
    font-size: 15px;
    margin: 4px 0 0;
    letter-spacing: 0.5px;
  }
  .hammer-art {
    position: absolute;
    left: 40px;
    top: 420px;
    width: 100px;
    height: 250px;
    background: linear-gradient(160deg, var(--ghost-grey), #1a1a1a);
    border-radius: 10px;
  }
  .contact {
    position: absolute;
    right: 32px;
    top: 560px;
    text-align: right;
    font-family: "Exo 2", Arial, sans-serif;
    color: var(--paper-white);
    font-size: 15px;
    line-height: 1.9;
    letter-spacing: 0.3px;
    white-space: nowrap;
  }
  .contact p { margin: 0; }
  .contact__phone { font-size: 19px; }
  .card--back .brand {
    top: 130px;
    font-size: 28px;
    gap: 20px;
  }
  .card--back .brand__square { width: 110px; height: 110px; }
  .work-photos {
    position: absolute;
    left: 30px;
    right: 30px;
    top: 440px;
    display: flex;
    gap: 20px;
  }
  .work-photo {
    flex: 1;
    height: 100px;
    background: linear-gradient(150deg, var(--photo-tone), #1e1b19);
    border: 2px solid var(--brand-orange);
  }
</style>
</head>
<body>
<main class="stage">
  <section class="card card--front" aria-label="Card front">
    <svg class="card__frame" viewBox="0 0 400 700" width="400" height="700" aria-hidden="true">
      <polygon fill="var(--brand-orange)" points="0,0 400,0 400,330 372,300 372,46 28,46 28,300 0,330"/>
      <g fill="var(--brand-orange)">
        <polygon points="0,350 28,320 28,360 0,390"/>
        <polygon points="0,410 28,380 28,420 0,450"/>
        <polygon points="0,470 28,440 28,480 0,510"/>
        <polygon points="400,350 372,320 372,360 400,390"/>
        <polygon points="400,410 372,380 372,420 400,450"/>
      </g>
    </svg>
    <div class="brand">
      <span class="brand__square"></span>
      <span class="brand__name">RTB CONTRACTING</span>
    </div>
    <div class="holder">
      <p class="holder__name">DEREK HOLLOWAY</p>
      <p class="holder__role">Managing Director</p>
    </div>
    <div class="hammer-art" role="img" aria-label="Faint dark grey hammer illustration"></div>
    <div class="contact">
      <p class="contact__phone">416-382-7164</p>
      <p class="contact__email">dholloway@mailbox-example.ca</p>
    </div>
  </section>

  <section class="card card--back" aria-label="Card back">
    <svg class="card__frame" viewBox="0 0 400 700" width="400" height="700" aria-hidden="true">
      <polygon fill="var(--paper-white)" points="0,640 400,600 400,625 0,665"/>
      <polygon fill="var(--paper-white)" points="0,680 400,640 400,700 0,700"/>
    </svg>
    <div class="brand">
      <span class="brand__square"></span>
      <span class="brand__name">RTB CONTRACTING</span>
    </div>
    <div class="work-photos">
      <div class="work-photo" role="img" aria-label="Photo of completed contracting work, project one"></div>
      <div class="work-photo" role="img" aria-label="Photo of completed contracting work, project two"></div>
      <div class="work-photo" role="img" aria-label="Photo of completed contracting work, project three"></div>
    </div>
  </section>
</main>
</body>
</html>
```